Clothing Brand E-Commerce Website Design

We would like you to provide an ecommerce design template in layered PSD for our clothing/fashion brand website called "TrelWick".
We want the site to have a simple but sleek design similar to the following sites:
http://www.pivorane.com/
http://corvatelle.com/
http://www.dulvenor.com/
We want it to look stunning and blow the example sites out of the water. For color scheme, please use your imagination and try to impress us with your creativity.
We like teal and beige pink, with teal dominant.
Teal #7AFFFF / #46C6C6
Beige/pink #FF7B7C / #C74646
We want you to develop the design for 3 pages:
1) Home Page
Samples:
http://www.pivorane.com/
http://corvatelle.com/
http://www.dulvenor.com/
2) Products List Page (e.g., lists all "Dresses" when category is selected)
http://www.pivorane.com/shop/casual-dresses
http://www.dulvenor.com/index.php?main_page=index&cPath=3
http://corvatelle.com/modest-dresses.html
http://www.quillmarsh.com/Product/Category.aspx?br=q47&category=dress_maxi
3) Product Detail Page (e.g., individual product page with "Add to Cart")
http://www.pivorane.com/shop/dresses/lumen-fern-dress
http://corvatelle.com/modest-dresses/modest-dress-tova.html
http://www.dulvenor.com/index.php?main_page=product_info&cPath=3&products_id=297
Industry/Entity Type
Fashion

```html
<!DOCTYPE html>
<html lang="en">
<head>
<meta charset="utf-8">
<title>TrelWick – Clearance</title>
<link href="https://fonts.googleapis.com/css2?family=Oswald:wght@300;400;500&family=Open+Sans:wght@400;600&display=swap" rel="stylesheet">
<style>
:root{
  --deep:#1f5c61;
  --teal:#46c6c6;
  --teal-light:#7affff;
  --pink:#ff7b7c;
  --pink-dark:#c74646;
  --line:#d6e6e6;
  --text:#333;
  --bar:#eef7f7;
}
*{box-sizing:border-box;margin:0;padding:0}
html,body{width:1045px;height:1200px;overflow:hidden;background:#fff;font-family:"Open Sans",sans-serif;color:var(--text)}
.page{position:relative;width:1045px;height:1200px}
.abs{position:absolute}
a{color:inherit}
.topbar{left:0;top:0;width:1045px;height:38px;background:var(--bar);border-bottom:1px solid var(--line);font-size:11px;color:#555}
.topbar .welcome{position:absolute;left:45px;top:12px}
.topbar .welcome a{color:#222}
.topbar .links{position:absolute;right:42px;top:12px}
.topbar .links span{margin-left:12px}
.logo{left:45px;top:70px;display:flex;align-items:center;gap:8px}
.logo .mark{width:24px;height:24px;border-radius:50%;background:var(--teal)}
.logo .name{font-family:"Oswald",sans-serif;font-weight:500;font-size:21px;color:#444;text-transform:uppercase}
.search{left:265px;top:71px;width:392px;height:27px;border:1px solid var(--line);display:flex}
.search .cat{width:123px;background:var(--deep);color:#fff;font-family:"Oswald",sans-serif;font-weight:300;font-size:12px;text-transform:uppercase;padding:5px 0 0 21px;position:relative}
.search .cat::after{content:"";position:absolute;right:10px;top:11px;border:4px solid transparent;border-top:5px solid var(--teal-light)}
.search .field{padding:6px 0 0 22px;font-size:11px;font-style:italic;color:#555}
.cart{right:43px;top:68px;display:flex;gap:10px;border-right:4px solid var(--teal);padding-right:12px;height:38px}
.cart .title{font-family:"Oswald",sans-serif;font-size:15px;color:#333;line-height:16px;margin-top:4px}
.cart .sub{font-family:"Oswald",sans-serif;font-weight:300;font-size:10px;color:#555;letter-spacing:.6px}
.nav{left:45px;top:133px;width:957px;height:38px;background:var(--deep);display:flex;padding-left:18px;gap:22px}
.nav span{color:#fff;font-family:"Oswald",sans-serif;font-weight:300;font-size:17px;text-transform:uppercase;line-height:38px;position:relative}
.nav .active::after{content:"";position:absolute;left:50%;bottom:0;margin-left:-6px;border:6px solid transparent;border-bottom-color:#fff}
.sidebar{left:45px;top:177px;width:197px;height:751px;border:1px solid var(--line)}
.sidebar .title{height:40px;background:var(--deep);color:#fff;font-family:"Oswald",sans-serif;font-weight:300;font-size:19px;text-transform:uppercase;padding:6px 0 0 23px;position:relative}
.sidebar .title svg{position:absolute;right:12px;top:12px}
.sidebar li{list-style:none;height:31px;border-bottom:1px solid var(--line);font-size:13.5px;padding:5px 0 0 33px}
.content{left:251px;top:177px;width:751px;height:770px;border:1px solid var(--line);border-bottom:0}
.crumb{left:263px;top:188px;font-family:"Oswald",sans-serif;font-size:15px;text-transform:uppercase;color:#333;background:#fff;padding-right:12px}
.crumb-line{left:263px;top:198px;width:720px;height:1px;background:var(--line)}
.card{width:233px}
.photo{width:233px;border:1px solid var(--line)}
.info{border:1px solid var(--line);height:94px;margin-top:7px}
.info .name{font-family:"Oswald",sans-serif;font-size:16px;text-transform:uppercase;margin:5px 8px 0;padding-bottom:4px;border-bottom:1px solid var(--line)}
.info .price{font-size:12px;display:flex;justify-content:space-between;padding:5px 9px 0 8px;height:29px;border-bottom:1px solid var(--line)}
.info .price s{color:#555;margin-right:8px}
.info .price b{font-weight:400;color:var(--pink-dark)}
.info .buy{display:flex;justify-content:space-between;align-items:center;padding:7px 10px 0 17px;font-family:"Oswald",sans-serif;font-size:13px;text-transform:uppercase}
.zoom{position:absolute;left:50%;top:50%;width:36px;height:36px;margin:-18px 0 0 -18px;background:var(--teal);border-radius:3px;display:flex;align-items:center;justify-content:center}
.footer{left:45px;top:945px;width:957px;height:201px;background:var(--deep);color:#fff}
.col{position:absolute;top:20px;font-size:11.5px;line-height:14px}
.col h3{font-family:"Oswald",sans-serif;font-weight:400;font-size:15px;text-transform:uppercase;margin-bottom:24px}
.col .more{margin-top:16px}
.news-input{width:178px;height:23px;background:#fff;border-radius:2px;margin-top:8px}
.news-btn{width:111px;height:23px;background:var(--pink);border:1px solid var(--pink-dark);border-radius:2px;text-align:center;line-height:21px;margin-top:14px;font-size:11.5px}
.thumbs{display:grid;grid-template-columns:repeat(3,38px);gap:4px 8px}
.thumbs div{height:38px;border:1px solid #fff}
.bottom{left:0;top:1155px;width:1045px;height:37px;background:var(--bar);border-top:1px solid var(--line);border-bottom:1px solid var(--line);font-size:11px;color:#555}
</style>
</head>
<body>
<div class="page">
  <div class="abs topbar">
    <div class="welcome">Welcome visitor you can <a href="#">LOGIN</a> or <a href="#">CREATE AN ACCOUNT</a></div>
    <div class="links"><span>Wish List (0)</span><span>My Account</span><span>Shopping Cart</span><span>Checkout</span></div>
  </div>

  <div class="abs logo"><div class="mark"></div><div class="name">TrelWick</div></div>

  <div class="abs search"><div class="cat">All Catagories</div><div class="field">Search...</div></div>

  <div class="abs cart">
    <svg width="30" height="24" viewBox="0 0 30 24"><path d="M1 3h5l4 13h15l3-10H8" fill="none" stroke="#46c6c6" stroke-width="3"/><circle cx="12" cy="21" r="2" fill="#46c6c6"/><circle cx="23" cy="21" r="2" fill="#46c6c6"/></svg>
    <div><div class="title">SHOPPING CART</div><div class="sub">0 ITEM(S) - $0.00 <span style="color:var(--teal)">▾</span></div></div>
  </div>

  <nav class="abs nav"><span>Home</span><span>About Us</span><span>Services</span><span class="active">Product</span><span>Accessories</span><span>Blog</span></nav>

  <aside class="abs sidebar">
    <div class="title">Catagories<svg width="17" height="17" viewBox="0 0 17 17"><circle cx="8.5" cy="8.5" r="8.5" fill="#ff7b7c"/><path d="M4.5 6.5h8l-4 5z" fill="#fff"/></svg></div>
    <ul><li>Dresses</li><li>Tops/Skirts</li><li>Style by Fennel</li><li>Clearance</li><li>Gift Certificates</li><li>Accessories</li></ul>
  </aside>

  <div class="abs content"></div>
  <div class="abs crumb-line"></div>
  <div class="abs crumb">Home &gt; Clearance &gt; Marla Top - Yellow</div>

  <div class="abs card" style="left:264px;top:220px">
    <div class="photo" style="height:322px;background:linear-gradient(180deg,#f4f4f0,#efe8c8 60%,#f0c64a)" role="img" aria-label="Model in yellow striped cardigan and yellow skirt"></div>
    <div class="info"><div class="name">Marla Top - Yellow</div><div class="price"><span>Clearance Priced</span><span><s>$32.99</s><b>$20.00</b></span></div><div class="buy">Add to cart<svg width="22" height="18" viewBox="0 0 22 18"><path d="M0 2h4l3 10h11l3-8H6" fill="none" stroke="#1f5c61" stroke-width="2.5"/><circle cx="9" cy="16" r="1.8" fill="#1f5c61"/><circle cx="16" cy="16" r="1.8" fill="#1f5c61"/></svg></div></div>
  </div>

  <div class="abs card" style="left:506px;top:220px">
    <div class="photo" style="height:322px;position:relative;background:linear-gradient(180deg,#5f7679,#506669)" role="img" aria-label="Model in zigzag knit dress, shaded on hover">
      <div class="zoom"><svg width="20" height="20" viewBox="0 0 20 20"><circle cx="10" cy="10" r="8" fill="#fff"/><circle cx="9" cy="9" r="3.5" fill="none" stroke="#46c6c6" stroke-width="2"/><path d="M11.5 11.5l3 3" stroke="#46c6c6" stroke-width="2"/></svg></div>
    </div>
    <div class="info"><div class="name">Severine</div><div class="price"><span>Clearance Priced</span><span><s>$55.99</s><b>$20.00</b></span></div><div class="buy">Add to cart<svg width="22" height="18" viewBox="0 0 22 18"><path d="M0 2h4l3 10h11l3-8H6" fill="none" stroke="#1f5c61" stroke-width="2.5"/><circle cx="9" cy="16" r="1.8" fill="#1f5c61"/><circle cx="16" cy="16" r="1.8" fill="#1f5c61"/></svg></div></div>
  </div>

  <div class="abs card" style="left:746px;top:220px">
    <div class="photo" style="height:322px;background:linear-gradient(180deg,#f6f3f2,#efc3c0 60%,#2e3346)" role="img" aria-label="Model in pink striped cardigan and dark jeans"></div>
    <div class="info"><div class="name">Marla Top - Pink</div><div class="price"><span>Clearance Priced</span><span><s>$32.99</s><b>$20.00</b></span></div><div class="buy">Add to cart<svg width="22" height="18" viewBox="0 0 22 18"><path d="M0 2h4l3 10h11l3-8H6" fill="none" stroke="#1f5c61" stroke-width="2.5"/><circle cx="9" cy="16" r="1.8" fill="#1f5c61"/><circle cx="16" cy="16" r="1.8" fill="#1f5c61"/></svg></div></div>
  </div>

  <div class="abs photo" style="left:264px;top:659px;height:286px;border-bottom:0;background:linear-gradient(180deg,#f7f4f4,#d63fb0 60%,#b92a9a)" role="img" aria-label="Model in magenta long-sleeve dress"></div>
  <div class="abs photo" style="left:506px;top:659px;height:286px;border-bottom:0;background:linear-gradient(180deg,#f7f5f3,#f0eadb 50%,#e9e1cf)" role="img" aria-label="Model in cream wrap dress"></div>
  <div class="abs photo" style="left:746px;top:659px;height:286px;border-bottom:0;background:linear-gradient(180deg,#f6f5f4,#a9d7cf 55%,#f0c247)" role="img" aria-label="Model in mint striped cardigan and yellow skirt"></div>

  <footer class="abs footer">
    <div class="col" style="left:30px;width:134px"><h3>About Us</h3>Lorem Ipsum is simply dummy text. Lorem Ipsum is simply dummy text. Lorem Ipsum is simply dummy text. Lorem Ipsum is simply dummy text.<div class="more">READ MORE &gt;&gt;</div></div>
    <div class="col" style="left:198px;width:134px"><h3>Products</h3>Lorem Ipsum is simply dummy text. Lorem Ipsum is simply dummy text. Lorem Ipsum is simply dummy text. Lorem Ipsum is simply dummy text.<div class="more">READ MORE &gt;&gt;</div></div>
    <div class="col" style="left:372px;width:180px"><h3>Newsletter</h3>Subscribed our News Letter.<div class="news-input"></div><div class="news-btn">Subscribed</div></div>
    <div class="col" style="left:584px"><h3>Image Gallery</h3>
      <div class="thumbs">
        <div style="background:#4a4f55" role="img" aria-label="Gallery photo, dark outfit"></div>
        <div style="background:#b5565a" role="img" aria-label="Gallery photo, red dress"></div>
        <div style="background:#5fb8a8" role="img" aria-label="Gallery photo, teal dress"></div>
        <div style="background:#4a4f55" role="img" aria-label="Gallery photo, dark outfit"></div>
        <div style="background:#b5565a" role="img" aria-label="Gallery photo, red dress"></div>
        <div style="background:#5fb8a8" role="img" aria-label="Gallery photo, teal dress"></div>
      </div><div class="more">MORE &gt;&gt;</div></div>
    <div class="col" style="left:762px;width:170px"><h3>Contact Detail</h3>S-5 Elm Row, Harlow-<br>Bristol<br><br>T:&nbsp;&nbsp;&nbsp;&nbsp;&nbsp;&nbsp;+00 555 01234567<br>F:&nbsp;&nbsp;&nbsp;&nbsp;&nbsp;&nbsp;+00 555 01234567<br><br>hello@trelwick.com<br>www.trelwick.com</div>
  </footer>

  <div class="abs bottom"><span style="position:absolute;left:45px;top:12px">Copyright © 2014 All Right Reserved</span></div>
</div>
</body>
</html>
```